website design for online company - registration of companies AUSTRALIA

website name: bizlodge88.com.au
purpose of the website: register NEW australian companies

once a client submits their order, our website will submit information to a government agency and in under 20 minutes, the client will receive their new company together with legal documentation:

key features:
- simplicity
- ease of use
- clarity
- fast
- competitive
- trust

our competitors:
www.swiftcharter.com.au
www.tallyforms.com.au

the website needs to be dynamic, clear and portray simplicity as the name suggests.

"register your company online with NBRO in 3 simple steps"
1 fill in a short form
2 submit payment
3 receive your company

headings - similar to our competitors but needs to be different.

Design only no coding

if you have any questions, feel free to ask

Target Market(s)

people in business

Industry/Entity Type

Government

Font styles to use
Serif

Requirements
Must have
• simple
creative
elegant
Nice to have
• top graphics

```html
<!DOCTYPE html>
<html lang="en">
<head>
<meta charset="utf-8">
<title>Bizlodge 88 — Register your company</title>
<link rel="stylesheet" href="https://fonts.googleapis.com/css2?family=Open+Sans:ital,wght@0,300;0,400;0,600;1,400&display=swap">
<style>
:root{
  --orange:#f7941d;
  --orange-deep:#ff7a00;
  --orange-light:#ffb300;
  --ink:#333333;
  --muted:#777777;
  --green:#7aa21a;
  --green-dark:#5f8a0e;
  --panel:#ffffff;
  --footer:#222222;
  --footer-bar:#2c2c2c;
  --footer-text:#dddddd;
}
*{box-sizing:border-box;margin:0;padding:0}
html,body{width:981px;height:1200px;overflow:hidden}
body{font-family:"Open Sans",Arial,sans-serif;color:var(--ink);background:#fff;position:relative}

.site-header{position:absolute;left:0;top:0;width:981px;height:86px;background:#fff;border-bottom:1px solid #e2e2e2}
.brand{position:absolute;left:121px;top:29px;font-size:25px;font-weight:600;color:var(--ink);letter-spacing:.2px;white-space:nowrap}
.main-nav{position:absolute;top:41px;left:0;width:981px}
.main-nav a{position:absolute;font-size:12px;font-weight:600;color:var(--ink);text-decoration:none;white-space:nowrap}
.main-nav a.active{color:var(--orange)}

.hero{position:absolute;left:0;top:87px;width:981px;height:378px;background:linear-gradient(#fff 60%,#f6f6f6)}
.hero-kicker{position:absolute;left:124px;top:100px;font-size:23px;font-weight:400;color:#333}
.hero-title{position:absolute;left:123px;top:124px;font-size:39px;font-weight:400;color:var(--orange)}
.hero-text{position:absolute;left:126px;top:172px;font-size:10px;line-height:16px;color:#666;width:320px}
.hero-dots{position:absolute;left:127px;top:218px;display:flex;gap:3px}
.hero-dots span{width:11px;height:11px;border-radius:50%;background:#d8d8d8}
.hero-dots span.on{background:#666}
.hero-art{position:absolute;left:540px;top:8px;width:310px;height:285px;border-radius:50%;
  background:radial-gradient(circle at 50% 55%,#d9d3cc 0%,#efece9 45%,rgba(255,255,255,0) 72%)}

.lower-bg{position:absolute;left:0;top:465px;width:981px;height:493px;background:radial-gradient(ellipse at 50% 40%,#fafafa,#e6e6e6 80%)}
.content-panel{position:absolute;left:112px;top:391px;width:750px;height:567px;background:var(--panel);border:1px solid #d4d4d4;border-bottom:none;border-radius:4px 4px 0 0}
.name-check{position:absolute;left:0;top:0;width:748px;height:53px;border-bottom:1px solid #eee}
.name-check label{position:absolute;left:76px;top:20px;font-size:12px;color:#444}
.name-check .field{position:absolute;left:273px;top:16px;width:272px;height:27px;border:1px solid #ccc;border-radius:2px;font-size:10px;color:#888;padding:6px 10px}
.name-check .btn{position:absolute;left:551px;top:16px;width:99px;height:27px;border-radius:2px;background:linear-gradient(var(--green),var(--green-dark));color:#fff;font-size:11.5px;font-weight:600;text-align:center;line-height:27px}

.steps{position:absolute;left:127px;top:457px;width:725px;height:222px;border-radius:4px;background:linear-gradient(var(--orange-light),var(--orange-deep))}
.steps h2{position:absolute;top:21px;width:100%;text-align:center;font-size:26px;font-weight:300;color:#fff}
.step{position:absolute;top:75px;width:220px;text-align:center;color:#fff}
.step svg{display:block;margin:0 auto;height:66px}
.step h3{margin-top:13px;font-size:15px;font-weight:600;letter-spacing:.2px;white-space:nowrap}
.step p{font-size:9.5px;line-height:15px;margin-top:1px}
.chev{position:absolute;top:77px}

.col{position:absolute;top:733px}
.col h2{font-size:20px;font-weight:400;color:#333}
.col.why h3{font-size:12px;font-weight:400;line-height:18px;margin-top:9px;color:#333;width:245px}
.col.why p{font-size:9.6px;line-height:16px;color:#777;margin-top:10px;width:242px}
.ticks{list-style:none;margin-top:10px}
.ticks li{font-size:10px;color:#555;height:23.5px;display:flex;align-items:center;gap:8px;white-space:nowrap}
.col.testi h2{color:var(--orange)}
.quote{position:relative;margin-top:9px;padding-left:19px;width:200px;font-size:9px;font-style:italic;line-height:17.5px;color:#555}
.quote .q{position:absolute;font-style:normal;font-weight:600;color:var(--orange);font-size:20px;line-height:1}
.author{margin-top:8px;padding-left:19px;font-size:11px;font-weight:600;color:#444}

.site-footer{position:absolute;left:0;top:958px;width:981px;height:195px;background:var(--footer);border-top:6px solid #d9d9d9}
.fcol{position:absolute;top:32px}
.fcol h4{font-size:14px;font-weight:400;color:#fff;margin-bottom:4px}
.fcol a{display:block;font-size:9.5px;color:var(--footer-text);text-decoration:none;line-height:18px}
.fcol.first a{font-size:10px;color:#fff}
.fcol p{font-size:9px;color:var(--footer-text)}
.social{display:flex;gap:6px;margin-top:14px}
.social span{width:18px;height:18px;border-radius:2px}
.footer-bar{position:absolute;left:0;top:1153px;width:981px;height:47px;background:var(--footer-bar)}
.footer-bar p{position:absolute;left:140px;top:18px;font-size:9.5px;color:#777}
</style>
</head>
<body>

<header class="site-header">
  <div class="brand">Bizlodge 88</div>
  <nav class="main-nav">
    <a class="active" style="left:393px">HOME</a>
    <a style="left:456px">ABOUT US</a>
    <a style="left:542px">SERVICES</a>
    <a style="left:623px">HOW IT WORKS</a>
    <a style="left:740px">FAQ</a>
    <a style="left:791px">CONTACT</a>
  </nav>
</header>

<section class="hero">
  <p class="hero-kicker">Nulla rhoncus dictum metus</p>
  <h1 class="hero-title">Proin dui lectus cursus</h1>
  <p class="hero-text">Curabitur tristique mi condimentum orci Phasellus pellentesque aliquam enim Proin dui lectus cursus eu mattis</p>
  <div class="hero-dots"><span class="on"></span><span></span><span></span><span></span></div>
  <div class="hero-art" role="img" aria-label="Illustration of a figure holding a large pen beside the word Register"></div>
</section>

<div class="lower-bg"></div>

<main class="content-panel">
  <form class="name-check">
    <label>Is your company name available?</label>
    <div class="field">type your company name</div>
    <div class="btn">CHECK NOW</div>
  </form>
</main>

<section class="steps">
  <h2>How it Works</h2>

  <div class="step" style="left:17px">
    <svg viewBox="0 0 70 70" fill="none" stroke="#fff" stroke-width="4">
      <path d="M6 4h44v34M6 4v52l10 10h24"/>
      <path d="M14 16h18M14 26h30M14 36h22M14 46h14"/>
      <circle cx="52" cy="52" r="14" fill="#fff" stroke="none"/>
      <path d="M45 52l5 5 9-10" stroke="#ff8a00" stroke-width="4"/>
    </svg>
    <h3>FILL IN A SHORT FORM</h3>
    <p>Lorem ipsum dolor sit amet consectetuer<br>adipiscing elit Nam cursus</p>
  </div>

  <svg class="chev" style="left:240px" width="24" height="56" viewBox="0 0 24 56" fill="none" stroke="#ffd27a" stroke-width="1.5"><path d="M2 2l20 26-20 26M8 2l14 18"/></svg>

  <div class="step" style="left:254px">
    <svg viewBox="0 0 80 70" fill="none" stroke="#fff" stroke-width="4">
      <rect x="4" y="14" width="56" height="40" rx="5"/>
      <path d="M4 26h56M12 36h22M12 44h14"/>
      <text x="52" y="60" fill="#fff" stroke="none" font-family="Open Sans,sans-serif" font-weight="700" font-size="56">$</text>
    </svg>
    <h3>SUBMIT PAYMENT</h3>
    <p>Lorem ipsum dolor sit amet consectetuer<br>adipiscing elit Nam cursus</p>
  </div>

  <svg class="chev" style="left:468px" width="24" height="56" viewBox="0 0 24 56" fill="none" stroke="#ffd27a" stroke-width="1.5"><path d="M2 2l20 26-20 26M8 2l14 18"/></svg>

  <div class="step" style="left:495px">
    <svg viewBox="0 0 70 70" fill="#fff">
      <circle cx="35" cy="9" r="7"/><path d="M22 28c0-8 6-11 13-11s13 3 13 11z"/>
      <circle cx="14" cy="46" r="7"/><path d="M1 66c0-8 6-11 13-11s13 3 13 11z"/>
      <circle cx="56" cy="46" r="7"/><path d="M43 66c0-8 6-11 13-11s13 3 13 11z"/>
      <path d="M35 28v10M35 38l-12 6M35 38l12 6" stroke="#fff" stroke-width="2" fill="none"/>
    </svg>
    <h3>RECEIVE YOUR COMPANY</h3>
    <p>Lorem ipsum dolor sit amet consectetuer<br>adipiscing elit Nam cursus</p>
  </div>
</section>

<section class="col why" style="left:133px">
  <h2>Why You Get</h2>
  <h3>Pellentesque faucibus Ut accumsan ultri-cies elit Maecenas at justo velit</h3>
  <p>Mauris vel lacus vitae felis vestibulum volutpat Etiam est nunc venenatis in tristique eu imperdiet ac nisl Cum sociis natoque penatibus et magnis dis parturi-ent montes nascetur ridiculus mus In iaculis facilisis massa Etiam eu urna Sed porta Suspendisse quam leo molestie sed luctus quis feugiat</p>
</section>

<section class="col choose" style="left:398px">
  <h2>Why Choose Us</h2>
  <ul class="ticks">
    <li><svg width="15" height="13" viewBox="0 0 15 13"><path d="M1 7l4 5 9-11" fill="none" stroke="var(--green)" stroke-width="3"/></svg>Mauris vel lacus vitae felis vestibulum</li>
    <li><svg width="15" height="13" viewBox="0 0 15 13"><path d="M1 7l4 5 9-11" fill="none" stroke="var(--green)" stroke-width="3"/></svg>Etiam est nunc venenatis in tristique</li>
    <li><svg width="15" height="13" viewBox="0 0 15 13"><path d="M1 7l4 5 9-11" fill="none" stroke="var(--green)" stroke-width="3"/></svg>Eu imperdiet Cum sociis natoque</li>
    <li><svg width="15" height="13" viewBox="0 0 15 13"><path d="M1 7l4 5 9-11" fill="none" stroke="var(--green)" stroke-width="3"/></svg>Dis parturient montes nascetur</li>
    <li><svg width="15" height="13" viewBox="0 0 15 13"><path d="M1 7l4 5 9-11" fill="none" stroke="var(--green)" stroke-width="3"/></svg>Ridiculus mus In iaculis facilisis massa</li>
    <li><svg width="15" height="13" viewBox="0 0 15 13"><path d="M1 7l4 5 9-11" fill="none" stroke="var(--green)" stroke-width="3"/></svg>Etiam eu urna Sed porta Suspendisse quam</li>
  </ul>
</section>

<section class="col testi" style="left:640px">
  <h2>Testimonials</h2>
  <blockquote class="quote">
    <span class="q" style="left:0;top:-1px">“</span>
    Etiam eu urna Sed porta Suspendisse quam leo molestie sed luctus quis feugiat in pede Fusce tellus Sed metus augue convallis et vehicula ut pulvinar eu ante Integer orci tellus tristique vitae consequat nec porta vel lectus Nulla sit amet diam <span class="q" style="position:relative;top:5px">”</span>
  </blockquote>
  <p class="author">By Author Name</p>
</section>

<footer class="site-footer">
  <div class="fcol first" style="left:152px"><h4>COMPANY</h4><a>What We Do</a><a>Why Choose Us</a><a>Features</a><a>Plans</a><a>Products</a></div>
  <div class="fcol" style="left:307px"><h4>SERVICES</h4><a>Aliquam nec erat</a><a>At purus cursus</a><a>Interdum Vestibulum</a><a>Ligula augue</a><a>Bibendum accumsan</a></div>
  <div class="fcol" style="left:483px"><h4>SUPPORT</h4><a>Aliquam nec erat</a><a>At purus cursus</a><a>Interdum Vestibulum</a><a>Ligula augue</a><a>Bibendum accumsan</a></div>
  <div class="fcol" style="left:648px"><h4>GET CONNECTED</h4><p>Please stay in touch with us on followings.</p>
    <div class="social"><span style="background:#3b5998"></span><span style="background:#3fa9e0"></span><span style="background:#1d75b3"></span><span style="background:#f26522"></span></div>
  </div>
</footer>
<div class="footer-bar"><p>© 2014 Company Name &nbsp;All right reserved &nbsp;Term of Use</p></div>

</body>
</html>
```